New business card design to go with our new logo

just want an eye-catching business card to go with our new logo. We are open to double sided or single sided. Just want it to have the following info on it. Whatever layout you think looks best.

First and Last Name
Title
Phone 801-555-0187
Address 312 W. Larkmoor Avenue Orem UT 84057
Email thecrew@meadowstailandkennel.example

Industry/Entity Type

Business

```html
<!DOCTYPE html>
<html lang="en">
<head>
<meta charset="utf-8">
<title>Meadows Tail &amp; Kennel — Business Card</title>
<link rel="stylesheet" href="https://fonts.googleapis.com/css2?family=Josefin+Sans:wght@400;600&family=Josefin+Slab:wght@600&display=swap">
<style>
  :root {
    --stage: #e9ebee;
    --card: #ffffff;
    --blue: #3f86c4;
    --orange: #d0702c;
    --shadow: rgba(0, 0, 0, 0.12);
  }
  * { margin: 0; padding: 0; box-sizing: border-box; }
  html, body {
    width: 1200px;
    height: 817px;
    overflow: hidden;
    background: var(--stage);
  }
  .business-card {
    position: absolute;
    left: 100px;
    top: 123px;
    width: 1000px;
    height: 571px;
    background: var(--card);
    box-shadow: 0 10px 30px var(--shadow);
    font-family: "Josefin Sans", sans-serif;
  }
  .card-wave {
    position: absolute;
    left: 0;
    top: 0;
    width: 1000px;
    height: 571px;
  }
  .contact-list {
    position: absolute;
    right: 462px;
    top: 180px;
    list-style: none;
    text-align: right;
    color: var(--orange);
    font-size: 19px;
    line-height: 1.3;
  }
  .contact-item {
    position: relative;
    padding-right: 66px;
    margin-bottom: 26px;
    min-height: 44px;
    display: flex;
    align-items: center;
    justify-content: flex-end;
  }
  .contact-icon {
    position: absolute;
    right: 0;
    top: 50%;
    transform: translateY(-50%);
    width: 44px;
    height: 44px;
  }
  .divider {
    position: absolute;
    left: 562px;
    top: 160px;
    width: 3px;
    height: 240px;
    background: var(--blue);
  }
  .brand {
    position: absolute;
    left: 600px;
    top: 170px;
    width: 350px;
    text-align: center;
  }
  .brand-circle {
    width: 170px;
    height: 170px;
    margin: 0 auto 18px;
    border-radius: 50%;
    border: 6px solid var(--orange);
  }
  .brand-name {
    font-family: "Josefin Slab", serif;
    font-weight: 600;
    font-size: 34px;
    color: var(--orange);
    letter-spacing: 1px;
  }
  .person {
    position: absolute;
    left: 88px;
    top: 432px;
  }
  .person-name {
    font-family: "Josefin Slab", serif;
    font-weight: 600;
    font-size: 40px;
    color: var(--blue);
  }
  .person-title {
    margin-top: 6px;
    font-family: "Josefin Sans", sans-serif;
    font-weight: 600;
    font-size: 22px;
    color: var(--orange);
  }
</style>
</head>
<body>
  <article class="business-card">
    <svg class="card-wave" viewBox="0 0 1000 571" aria-hidden="true">
      <path d="M0 392 C150 372 300 360 420 395 C540 430 600 500 700 496 C800 492 880 470 1000 466"
            fill="none" stroke="var(--blue)" stroke-width="10"/>
      <path d="M0 404 C150 386 300 378 420 412 C540 446 600 512 700 510 C800 507 880 482 1000 476"
            fill="none" stroke="var(--orange)" stroke-width="5"/>
    </svg>

    <ul class="contact-list">
      <li class="contact-item">
        <span class="contact-text">801-555-0187</span>
        <svg class="contact-icon" viewBox="0 0 44 44" aria-hidden="true">
          <circle cx="22" cy="22" r="19" fill="none" stroke="var(--blue)" stroke-width="2"/>
          <path d="M13 19 Q22 12 31 19 L29 22 L25 21 L25 19 Q22 18 19 19 L19 21 L15 22 Z M16 24 H28 V30 H16 Z" fill="var(--blue)"/>
        </svg>
      </li>
      <li class="contact-item">
        <span class="contact-text">312 W. Larkmoor Avenue<br>Orem UT 84057</span>
        <svg class="contact-icon" viewBox="0 0 44 44" aria-hidden="true">
          <circle cx="22" cy="22" r="19" fill="none" stroke="var(--blue)" stroke-width="2"/>
          <path d="M22 32 C17 25 15 22 15 19 A7 7 0 0 1 29 19 C29 22 27 25 22 32 Z" fill="none" stroke="var(--blue)" stroke-width="2"/>
          <circle cx="22" cy="19" r="2.5" fill="var(--blue)"/>
        </svg>
      </li>
      <li class="contact-item">
        <span class="contact-text">thecrew@meadowstailandkennel.example</span>
        <svg class="contact-icon" viewBox="0 0 44 44" aria-hidden="true">
          <circle cx="22" cy="22" r="19" fill="none" stroke="var(--blue)" stroke-width="2"/>
          <text x="22" y="28" text-anchor="middle" font-family="Josefin Sans, sans-serif" font-size="18" font-weight="600" fill="var(--blue)">@</text>
        </svg>
      </li>
    </ul>

    <div class="divider"></div>

    <div class="brand">
      <div class="brand-circle"></div>
      <div class="brand-name">Meadows Tail &amp; Kennel</div>
    </div>

    <div class="person">
      <div class="person-name">Mark Ellison</div>
      <div class="person-title">- CEO</div>
    </div>
  </article>
</body>
</html>
```